Logo, Web and Mobile Designs for enterprise social media platform

All the details are in the attached document, please start reading the scope document first which explains what is this project about and the details about the needed deliverables, after that please read the UI_Requirements document which will detail what is expected regarding the coded web version since this is a coded contest, it is very important that you meet the UI requirements or suggest something else but we will need to agree first before working on the coded version

Good Luck

Target Market(s)

Enterprise Social Media

Industry/Entity Type

Media

Coding

Coded - Design and coding required

Number of Pages Required

5+ page

Font styles to use
Sans Serif

Requirements
Must have
• All the must haves are listed in the scope document so please check before you start

```html
<!DOCTYPE html>
<html lang="en">
<head>
<meta charset="utf-8">
<title>Teamora – Timeline</title>
<link href="https://fonts.googleapis.com/css2?family=Roboto:wght@300;400;500;700&family=Roboto+Condensed:wght@700&display=swap" rel="stylesheet">
<style>
:root{
  --page:#e9eaeb;
  --white:#ffffff;
  --blue:#2196cb;
  --link:#2a9fd6;
  --navy:#2f4f8f;
  --orange:#f4a10b;
  --text:#444;
  --line:#dcdcdc;
  --star:#f2a71b;
  --fb:#3b5998;
  --tw:#2cb9ea;
  --gp:#dd4b39;
}
*{margin:0;padding:0;box-sizing:border-box}
html,body{width:687px;height:1200px;overflow:hidden}
body{background:var(--page);font-family:"Roboto",Arial,sans-serif;color:var(--text);position:relative;font-size:7px}
.abs{position:absolute}
/* header */
.topbar{left:0;top:0;width:687px;height:40px;background:var(--white);border-bottom:1px solid var(--line)}
.brand{left:56px;top:10px;display:flex;align-items:center;gap:5px;font-size:17px;font-weight:500;color:var(--blue)}
.brand-dot{width:18px;height:18px;border-radius:50%;background:var(--orange)}
.mainnav{left:320px;top:0;height:40px;display:flex}
.mainnav a{display:flex;align-items:center;justify-content:center;gap:5px;border-left:1px solid #eee;font-size:7px;color:#666;text-decoration:none;text-transform:uppercase;white-space:nowrap}
.mainnav svg{width:9px;height:9px;fill:#999}
.signin{left:583px;top:13px;width:48px;height:17px;background:var(--orange);color:#fff;font-size:7px;font-weight:500;display:flex;align-items:center;justify-content:center}
/* hero */
.hero{left:56px;top:54px;width:574px;height:258px;background:var(--white);border:1px solid #ddd}
.hero-img{left:3px;top:2px;width:567px;height:231px;background:linear-gradient(90deg,#1a2438 0%,#25365c 30%,#8a4a2a 55%,#b56a35 75%,#6a3a2a 100%)}
.hero-title{right:16px;top:112px;font-family:"Roboto Condensed",Arial,sans-serif;font-weight:700;color:#fff;font-size:27px;line-height:29px}
.tabs{left:10px;top:240px;display:flex;font-size:7px;color:#333}
.tabs span{padding:5px 8px 6px;border-right:1px solid #eee}
.tabs .on{border-bottom:2px solid var(--navy)}
.dots{right:6px;top:243px;display:flex;gap:4px;align-items:center}
.dots i{width:5px;height:5px;border-radius:50%;background:#333}
.dots i.on{width:9px;height:9px;background:#fff;border:2px solid var(--navy)}
/* left */
.panel{left:56px;width:160px;background:var(--white);border:1px solid #ddd}
.panel-head{height:19px;border-bottom:1px solid #e4e4e4;padding:0 6px;display:flex;justify-content:space-between;align-items:center;font-size:7px;text-transform:uppercase;color:#555}
.panel-head b{font-weight:400;color:#aaa}
.avatar{border-radius:50%;flex:none;background:linear-gradient(#c9cfd6,#6b7684)}
.name{color:var(--link);font-size:7px}
.lorem{font-style:italic;font-size:6px;line-height:11px;color:#555}
.stars{color:var(--star);font-size:6px}
.person{display:flex;gap:8px;padding:4px 8px;align-items:center}
.gp-row{padding:8px;font-size:6.3px;line-height:9px;display:flex;gap:8px}
.gp-row i{width:6px;height:6px;border-radius:50%;background:#bbb;flex:none;margin-top:1px}
.grid{display:grid;grid-template-columns:repeat(3,48px);gap:2px;padding:7px 6px}
.grid div{height:48px}
.social{left:63px;top:938px;display:flex;gap:6px}
.social div{width:46px;height:46px;color:#fff;font-size:7px;text-align:center;line-height:9px;padding-top:6px}
.social s{display:block;width:8px;height:8px;background:rgba(255,255,255,.9);margin:0 auto 3px;text-decoration:none}
.notify{background:var(--orange);color:#fff;text-align:center;font-size:6px;line-height:10.5px;padding:7px 10px}
/* right */
.stream{left:239px;top:328px;width:391px;height:762px;background:var(--blue)}
.stream h2{position:absolute;left:17px;top:9px;font-weight:400;font-size:13px;color:#fff}
.card{position:absolute;left:19px;width:354px;background:#fff}
.actions{border-top:1px solid #e2e2e2;height:17px;display:flex;gap:12px;align-items:center;padding-left:7px;font-size:6px;text-transform:uppercase;color:#555}
.actions span::before{content:"";display:inline-block;width:5px;height:5px;background:#999;margin-right:4px;border-radius:1px}
.post-head{display:flex;gap:6px;padding:7px 8px 0}
.post-head .dot{width:14px;height:14px;border-radius:50%;background:var(--orange)}
.post-head p{font-size:6.5px;line-height:7.5px;color:var(--navy)}
.post-body{font-size:6.4px;line-height:11px;color:#555;padding:4px 20px 6px 10px;height:51px}
.article{display:flex;gap:14px;padding:3px}
.article .ph{width:126px;height:114px;flex:none}
.article h3{font-weight:400;font-size:9px;line-height:13px;color:#444;margin-top:7px}
.meta{font-style:italic;font-size:6.5px;color:#555;margin:7px 0 6px}
.article p.b{font-size:6px;line-height:11.5px;color:#555}
.more{font-size:6px;color:var(--link);text-decoration:underline;display:block;margin-top:6px}
.pager{left:85px;top:712px;display:flex;gap:5px}
.pager span{background:#fff;color:#333;font-size:6.5px;font-weight:500;height:14px;min-width:14px;padding:0 4px;display:flex;align-items:center;justify-content:center}
/* footer */
.footer{left:0;top:1115px;width:687px;height:85px;background:var(--blue);color:#fff;text-align:center}
.foot-icons{display:flex;gap:7px;justify-content:center;margin-top:17px}
.foot-icons i{width:14px;height:14px;background:#fff;border-radius:2px}
.foot-links{font-size:7.5px;margin-top:9px}
.copy{font-size:7.5px;margin-top:8px}
</style>
</head>
<body>
<header class="abs topbar">
  <div class="abs brand"><span class="brand-dot"></span>Teamora</div>
  <nav class="abs mainnav">
    <a style="width:73px"><svg viewBox="0 0 10 10"><rect x="0" y="2" width="10" height="7"/></svg>Messages</a>
    <a style="width:64px"><svg viewBox="0 0 10 10"><circle cx="5" cy="3" r="2.5"/><rect x="1" y="6" width="8" height="4" rx="2"/></svg>People</a>
    <a style="width:66px"><svg viewBox="0 0 10 10"><ellipse cx="5" cy="5" rx="5" ry="3.5"/></svg>Groups</a>
    <a style="width:57px"><svg viewBox="0 0 10 10"><rect x="0.5" y="1" width="9" height="9"/></svg>Events</a>
  </nav>
  <div class="abs signin">SIGN IN</div>
</header>

<section class="abs hero">
  <div class="abs hero-img" role="img" aria-label="Speaker in a dark suit addressing a large blurred conference audience"></div>
  <div class="abs hero-title">SOCIAL MEDIA<br>PLATFORM</div>
  <div class="abs tabs"><span class="on">Timeline</span><span>About</span><span>Welcome</span><span>Chat</span><span>More ▾</span></div>
  <div class="abs dots"><i class="on"></i><i></i><i></i><i></i></div>
</section>

<aside>
  <div class="abs panel" style="top:328px;height:88px">
    <div class="panel-head">Profile<b>›</b></div>
    <div style="display:flex;gap:10px;padding:6px 8px 0">
      <div class="avatar" style="width:44px;height:44px" role="img" aria-label="Profile photo"></div>
      <div style="padding-top:4px"><div class="name">JOHN DOE</div><div class="lorem" style="margin-top:3px">Lorem ipsum dolor sit amet, consectetur adipiscing elit, sed do</div><div class="stars" style="margin-top:2px">★★★☆☆</div></div>
    </div>
  </div>
  <div class="abs panel" style="top:428px;height:92px">
    <div class="panel-head">General Panels<b>›</b></div>
    <div class="gp-row" style="border-bottom:1px solid #eee"><i></i>Lorem ipsum dolor sit amet timeti ergo sum Lorem ipsum dolor sit amet timeti dolor sit amet timeti</div>
    <div class="gp-row" style="color:var(--navy)"><i></i>http://www.teamora.com/</div>
  </div>
  <div class="abs panel" style="top:530px;height:199px">
    <div class="panel-head">People List<b>›</b></div>
    <div class="person" style="margin-top:6px"><div class="avatar" style="width:42px;height:42px" role="img" aria-label="Member photo"></div><div><div class="lorem">Lorem ipsum dolor sit amet, consectetur adipiscing elit, sed do</div><div class="name" style="margin-top:4px">JOHN DOE &nbsp;<span class="stars">★★★☆☆</span></div></div></div>
    <div class="person" style="margin-top:6px"><div class="avatar" style="width:42px;height:42px" role="img" aria-label="Member photo"></div><div><div class="lorem">Lorem ipsum dolor sit amet, consectetur adipiscing elit, sed do</div><div class="name" style="margin-top:4px">JOHN DOE &nbsp;<span class="stars">★★★☆☆</span></div></div></div>
    <div class="person" style="margin-top:6px"><div class="avatar" style="width:42px;height:42px" role="img" aria-label="Member photo"></div><div><div class="lorem">Lorem ipsum dolor sit amet, consectetur adipiscing elit, sed do</div><div class="name" style="margin-top:4px">JOHN DOE &nbsp;<span class="stars">★★★☆☆</span></div></div></div>
  </div>
  <div class="abs panel" style="top:742px;height:185px">
    <div class="panel-head">User Picker<b>›</b></div>
    <div class="grid">
      <div style="background:linear-gradient(#6a3a2e,#2e1d1a)" role="img" aria-label="Concert crowd"></div>
      <div style="background:linear-gradient(#c9c7b8,#7c7a5c)" role="img" aria-label="Person on a road"></div>
      <div style="background:linear-gradient(#5c6b3e,#2f3a22)" role="img" aria-label="Woman with headphones"></div>
      <div style="background:linear-gradient(#9cc06a,#4f7a2e)" role="img" aria-label="People in a park"></div>
      <div style="background:linear-gradient(#d8cfc2,#9b8875)" role="img" aria-label="Couple with phone"></div>
      <div style="background:linear-gradient(#5a2a6a,#b23a5e)" role="img" aria-label="Band on stage"></div>
      <div style="background:linear-gradient(#6a7ab2,#b25a8a)" role="img" aria-label="Party crowd"></div>
      <div style="background:linear-gradient(#7a5a4a,#3a2a22)" role="img" aria-label="Girl with curly hair"></div>
      <div style="background:linear-gradient(#a8b85a,#5e7a2a)" role="img" aria-label="Smiling woman outdoors"></div>
    </div>
  </div>
  <div class="abs social">
    <div style="background:var(--fb)"><s></s>68,876<br>Fans</div>
    <div style="background:var(--tw)"><s></s>65<br>Followers</div>
    <div style="background:var(--gp)"><s></s>8,961<br>Followers</div>
  </div>
  <div class="abs panel" style="top:997px;height:93px;border-color:var(--orange)">
    <div class="panel-head">Notifications<b>›</b></div>
    <div class="notify">Lorem ipsum dolor sit amet, consectetur adipiscing elit, sed do eiusmod tempor incididunt ut labore et dolore magna aliqua. Ut enim ad minim veniam, quis nostrud exercitation ullamco</div>
  </div>
</aside>

<main class="abs stream">
  <h2>Posts and Comments</h2>
  <div class="card" style="top:32px;height:178px">
    <div style="margin:6px 6px 0;height:117px;background:linear-gradient(90deg,#d7d9dc 0%,#8d9093 40%,#3e3f42 60%,#c48ab8 85%,#e6b2d4 100%)" role="img" aria-label="Modern office lounge with a wall of screens"></div>
    <div style="padding:7px 7px 0;font-size:8.5px;line-height:12px;color:#555"><span style="color:var(--navy)">Teamora.</span> changed their <span style="color:var(--navy)">cover photo.</span><br>3 minutes ago</div>
    <div class="actions" style="position:absolute;bottom:0;width:100%"><span>Like</span><span>Comment</span><span>Share</span></div>
  </div>
  <div class="card" style="top:221px;height:91px">
    <div class="post-head"><div class="dot"></div><p>Teamora<br>December 12, 2013</p></div>
    <div class="post-body">Lorem ipsum dolor sit amet, consectetur adipiscing elit, sed do eiusmod tempor incididunt ut labore et dolore magna aliqua. Ut enim ad minim veniam, quis nostrud exercitation ullamco laboris nisi ut aliquip ex ea commodo consequat. m</div>
    <div class="actions"><span>Like</span><span>Comment</span><span>Share</span></div>
  </div>
  <div class="card" style="top:324px;height:91px">
    <div class="post-head"><div class="dot"></div><p>Teamora<br>December 12, 2013</p></div>
    <div class="post-body">Lorem ipsum dolor sit amet, consectetur adipiscing elit, sed do eiusmod tempor incididunt ut labore et dolore magna aliqua. Ut enim ad minim veniam, quis nostrud exercitation ullamco laboris nisi ut aliquip ex ea commodo consequat. m</div>
    <div class="actions"><span>Like</span><span>Comment</span><span>Share</span></div>
  </div>
  <div class="card" style="top:428px">
    <div class="article">
      <div class="ph" style="background:linear-gradient(135deg,#c8ccd2,#5f6e80)" role="img" aria-label="Two colleagues reviewing documents"></div>
      <div style="padding-right:20px"><h3>Nemo enim ipsam voluptatem quia voluptas sit aspernatur aut</h3><div class="meta">▦ March 25, 2015 &nbsp;&nbsp;&nbsp; ○ 2 comments</div><p class="b">Lorem ipsum dolor sit amet, consectetur adipiscing elit, sed do eiusmod tempor incididunt ut labore et dolore magna aliqua. Ut enim ad minim Lorem ipsum dolor sit amet,</p><span class="more">LEARN MORE &gt;&gt;</span></div>
    </div>
  </div>
  <div class="card" style="top:560px">
    <div class="article">
      <div class="ph" style="background:linear-gradient(135deg,#b7c7d4,#8a6a5a 60%,#5e7a9a)" role="img" aria-label="Group of people holding up photo frames"></div>
      <div style="padding-right:20px"><h3>Nemo enim ipsam voluptatem quia voluptas sit aspernatur aut</h3><div class="meta">▦ March 25, 2015 &nbsp;&nbsp;&nbsp; ○ 2 comments</div><p class="b">Lorem ipsum dolor sit amet, consectetur adipiscing elit, sed do eiusmod tempor incididunt ut labore et dolore magna aliqua. Ut enim ad minim Lorem ipsum dolor sit amet,</p><span class="more">LEARN MORE &gt;&gt;</span></div>
    </div>
  </div>
  <div class="abs pager"><span style="padding:0 9px">Prev</span><span>1</span><span>2</span><span>3</span><span>4</span><span>5</span><span>6</span><span>...</span><span>22</span><span style="padding:0 8px">Next</span></div>
</main>

<footer class="abs footer">
  <div class="foot-icons"><i></i><i></i><i></i><i></i><i></i></div>
  <div class="foot-links">Home &nbsp;/&nbsp; Contact &nbsp;/&nbsp; Topics &nbsp;/&nbsp; Posts and Comments &nbsp;/&nbsp; Discussion &nbsp;/&nbsp; Videos Links</div>
  <div class="copy">Copyright @ 2015 - 2015.Teamora. All Rights Reserved.</div>
</footer>
</body>
</html>
```